Business cards, stationary and email tagline
Tovarin Meadow
Professional
Lena Ortwick
P.O. Box 81
Harlow Bend, Pa 17418
855-55-PLUMB
lena@tovarinmeadow.com
www.tovarinmeadow.com
I would like to be able to change names etc on the business cards for other workers.
Something clean such as our logo, open to your designs.

```html
<!DOCTYPE html>
<html lang="en">
<head>
<meta charset="utf-8">
<title>Tovarin Meadow – Business Card</title>
<link href="https://fonts.googleapis.com/css2?family=PT+Serif:wght@400;700&display=swap" rel="stylesheet">
<style>
  :root {
    --page-bg: #e9e4dc;
    --card-bg: #ffffff;
    --brand-blue: #2a57a5;
    --brand-blue-dark: #1b3f80;
    --accent-grey: #9a9ea6;
    --text-grey: #4a4d52;
    --divider: #b9bcc2;
  }
  * { box-sizing: border-box; margin: 0; padding: 0; }
  html, body {
    width: 1200px; height: 780px; overflow: hidden;
    background: var(--page-bg);
    font-family: "PT Serif", Georgia, serif;
  }
  .card {
    position: absolute; left: 75px; top: 90px;
    width: 1050px; height: 600px;
    background: var(--card-bg);
    border-radius: 34px;
    overflow: hidden;
    box-shadow: 0 10px 30px rgba(0,0,0,0.18);
  }
  .swoosh { position: absolute; }
  .swoosh--top { left: 0; top: 0; }
  .swoosh--bottom { right: 0; bottom: 0; transform: rotate(180deg); }
  .brand {
    position: absolute; top: 150px; left: 0; width: 100%;
    display: flex; align-items: center; justify-content: center; gap: 22px;
  }
  .brand__dot {
    width: 46px; height: 46px; border-radius: 50%;
    background: var(--brand-blue);
  }
  .brand__name {
    font-size: 76px; font-weight: 400; color: var(--brand-blue);
    letter-spacing: 1px;
  }
  .details {
    position: absolute; top: 330px; left: 170px;
    display: flex; align-items: stretch;
  }
  .person {
    text-align: right; padding-right: 26px;
    border-right: 2px solid var(--divider);
    color: var(--text-grey); font-size: 21px; line-height: 1.35;
  }
  .person__name {
    color: var(--brand-blue); font-weight: 700; font-size: 29px;
    margin-bottom: 2px;
  }
  .person__title { margin-bottom: 18px; }
  .contact { list-style: none; padding-left: 22px; color: var(--text-grey); font-size: 21px; }
  .contact li { display: flex; align-items: center; gap: 14px; height: 34px; }
  .contact svg { width: 22px; height: 22px; fill: var(--accent-grey); flex: none; }
</style>
</head>
<body>
  <div class="card">
    <svg class="swoosh swoosh--top" width="330" height="230" viewBox="0 0 330 230">
      <defs>
        <linearGradient id="blueSweep" x1="0" y1="0" x2="1" y2="1">
          <stop offset="0" stop-color="#1b3f80"/>
          <stop offset="1" stop-color="#3d6cc0"/>
        </linearGradient>
      </defs>
      <path d="M0 0 H300 C180 25 70 90 0 200 Z" fill="url(#blueSweep)"/>
      <path d="M0 215 C70 105 180 38 320 8" fill="none" stroke="var(--accent-grey)" stroke-width="6"/>
    </svg>
    <svg class="swoosh swoosh--bottom" width="330" height="230" viewBox="0 0 330 230">
      <path d="M0 0 H300 C180 25 70 90 0 200 Z" fill="url(#blueSweep)"/>
      <path d="M0 215 C70 105 180 38 320 8" fill="none" stroke="var(--accent-grey)" stroke-width="6"/>
    </svg>

    <div class="brand">
      <span class="brand__dot"></span>
      <span class="brand__name">Tovarin Meadow</span>
    </div>

    <div class="details">
      <div class="person">
        <div class="person__name">Lena Ortwick</div>
        <div class="person__title">General Manager</div>
        <div>P.O. Box 81</div>
        <div>Harlow Bend, Pa 17418</div>
      </div>
      <ul class="contact">
        <li>
          <svg viewBox="0 0 24 24"><path d="M6.6 10.8a15 15 0 0 0 6.6 6.6l2.2-2.2c.3-.3.7-.4 1-.2 1.1.4 2.3.6 3.6.6.6 0 1 .4 1 1V20c0 .6-.4 1-1 1A17 17 0 0 1 3 4c0-.6.4-1 1-1h3.5c.6 0 1 .4 1 1 0 1.3.2 2.5.6 3.6.1.3 0 .7-.2 1z"/></svg>
          855-55-PLUMB
        </li>
        <li>
          <svg viewBox="0 0 24 24"><path d="M7 1h10a2 2 0 0 1 2 2v18a2 2 0 0 1-2 2H7a2 2 0 0 1-2-2V3a2 2 0 0 1 2-2zm0 3v14h10V4zm5 15.5a1 1 0 1 0 0 2 1 1 0 0 0 0-2z"/></svg>
          717-555-0142
        </li>
        <li>
          <svg viewBox="0 0 24 24"><path d="M6 2h9l3 3v5h1a3 3 0 0 1 3 3v7a2 2 0 0 1-2 2H4a2 2 0 0 1-2-2v-7a3 3 0 0 1 3-3h1zm2 2v6h8V6h-2V4zm-1 10v2h10v-2z"/></svg>
          717-555-0187
        </li>
        <li>
          <svg viewBox="0 0 24 24"><path d="M2 5h20v14H2zm2 2v.5l8 5 8-5V7zm0 2.8V17h16V9.8l-8 5z"/></svg>
          lena@tovarinmeadow.com
        </li>
      </ul>
    </div>
  </div>
</body>
</html>
```